60 Ways to de-stress Poster

I would like a poster ( A4 full colour) with a list of 60 ways to destress. I would like the design to be clean and stylish (not cartoonish)

My Target market is stressed out mums so I want the poster to feel inspirational and relaxing to look at.

I have added a sample of something I like - but open to other ideas

Finished art would be print ready pdf

Target Market(s)

Mums who are stressed out - mainly new mums. I want this to be a poster that someone would happily put up that looks more like artwork.

Requirements
Must have
• My logo elements and colours but happy to incorporate other colours that blend well into it.

Colours:
Bright green: Pantone 376
Bright green as CMYK: c: 45.2% m: 0% y: 100% k: 0%

Logo text large grey: 70% black
Logo text strapline: 75% black
Tree: 80% black

Fonts:
Logo 'Willowbrook Calm': Verdana
Logo 'Counselling & coaching services for mums': Gill Sans Light
Should not have
• No cartoonish images - I want it very clean and stylish

```html
<!DOCTYPE html>
<html lang="en">
<head>
<meta charset="utf-8">
<title>60 Ways to De-Stress – Willowbrook Calm</title>
<link href="https://fonts.googleapis.com/css2?family=Lato:ital,wght@0,400;0,700;1,400;1,700&family=Open+Sans:wght@600;700&display=swap" rel="stylesheet">
<style>
  :root {
    --green: #8cc63f;
    --grey-brand: #5a5a5a;
    --grey-strap: #4d4d4d;
    --mark: #444444;
    --stripe-light: #ffffff;
    --stripe-dark: #e4e4e4;
    --panel: #ffffff;
  }
  * { margin: 0; padding: 0; box-sizing: border-box; }
  html, body { width: 849px; height: 1200px; overflow: hidden; }
  body {
    position: relative;
    background: repeating-linear-gradient(
      -35deg,
      var(--stripe-dark) 0 46px,
      var(--stripe-light) 46px 92px
    );
    font-family: "Lato", Arial, sans-serif;
  }
  .brand {
    position: absolute;
    top: 112px;
    left: 0;
    width: 849px;
    text-align: center;
  }
  .brand__name {
    display: inline-flex;
    align-items: center;
    gap: 14px;
    font-family: "Open Sans", Verdana, sans-serif;
    font-weight: 600;
    font-size: 42px;
    line-height: 1.1;
    color: var(--grey-brand);
    letter-spacing: -0.5px;
  }
  .brand__dot {
    width: 20px; height: 20px; border-radius: 50%;
    background: var(--mark);
  }
  .brand__strap {
    font-family: "Lato", sans-serif;
    font-weight: 400;
    font-size: 22px;
    line-height: 1.1;
    color: var(--grey-strap);
  }
  .poster {
    position: absolute;
    left: 61px;
    top: 218px;
    width: 727px;
    height: 950px;
    background: var(--panel);
    padding: 24px 15px 0;
    box-shadow: 0 2px 6px rgba(0,0,0,0.08);
    overflow: hidden;
  }
  .poster__title {
    font-family: "Open Sans", Arial, sans-serif;
    font-weight: 700;
    color: var(--green);
    font-size: 62px;
    line-height: 1;
    letter-spacing: -1px;
    white-space: nowrap;
    text-align: center;
    margin-bottom: 12px;
  }
  .ways {
    color: var(--green);
    font-size: 26.5px;
    line-height: 33px;
    text-align: justify;
  }
  .ways .it { font-style: italic; }
  .ways .bd { font-weight: 700; }
  .ways .up { text-transform: uppercase; }
</style>
</head>
<body>
  <header class="brand">
    <div class="brand__name"><span>Willowbrook Calm</span><span class="brand__dot"></span></div>
    <div class="brand__strap">counselling &amp; coaching for mums</div>
  </header>

  <main class="poster">
    <h1 class="poster__title">60 WAYS TO DE STRESS</h1>
    <p class="ways">
      <span class="it">Put on some music and dance</span> | <span class="bd">Make a gratitude list</span> | Eat something mindfully | <span class="it">Go to the park</span> | Light a scented candle | <span class="it">Buy yourself flowers</span> | Listening to music | <span class="bd">Call or visit a friend</span> | <span class="bd">Take a nap</span> | <span class="up">Take some deep breaths</span> | <span class="it">Take a mini mental holiday</span> | <span class="bd">Watch the clouds go by</span> | Have a bath | <span class="it">Meditate</span> | Write in a journal | <span class="bd">Go for a walk</span> | Plant a tree | <span class="it">Swing on a swing</span> | Forgive someone | <span class="bd">Write a poem</span> | Hug someone | <span class="bd">Fake a smile</span> | Gaze at the stars | <span class="it">Play a game</span> | Stand up and stretch | <span class="up">Paint a picture</span> | <span class="it">Read a book</span> | Look at a work of art | Bake some cookies | <span class="up">Go for a bike ride</span> | <span class="bd">Review your achievements</span> | Relive happy memories | <span class="it">Get a haircut</span> | Pat a dog | <span class="up">Volunteer your time</span> | Perform an act of kindness | <span class="it">Give yourself a time-out</span> | Make yourself a cup of tea | <span class="up">Listen to a guided relaxation MP3</span> | Watch a funny movie | <span class="it">Disconnect from technology</span> | Colour in | <span class="bd up">Play in the park</span> | Take a class at the gym | Get a massage | <span class="bd it">De-clutter a drawer</span> | Take a long drive | <span class="it">Borrow a book from the library</span> | <span class="bd">Go on a picnic</span> | <span class="it">Visit a farmers market</span> | Vent | <span class="up">Live for today</span> | Ask for help | <span class="it up">Create some routines</span> | <span class="it">Scale down your to do list</span> | <span class="bd">Accept what you can’t change</span> | <span class="up">Compliment yourself often</span> | <span class="it">Outsource if you can</span> | <span class="it">Write positive self-statements</span> | <span class="bd">Try Progressive Muscle Relaxation</span>
    </p>
  </main>
</body>
</html>
```